Service company standing banner design

We are an existing company that just updated our logo. We are attending some oportunity summits in the near future and want a new crisp clean look on our three banners that will be placed in the back of our small booth. The summits we are attending are designed to give local companies opportunities on a prokect we have been awarded to construct in their area. These banners should communicate who we are with no questions when people see them. One banner shall list our services. One to list our values and one to state our goals. All these while being appealing to the eye and using picture of nature. Attached are copies of what we are to replace. also the new logo and the original background pictures in the existing banners

```html
<!DOCTYPE html>
<html lang="en">
<head>
<meta charset="utf-8">
<title>Norvale Services – Booth Banners</title>
<link href="https://fonts.googleapis.com/css2?family=Signika:wght@600&display=swap" rel="stylesheet">
<style>
  :root {
    --backdrop: #c8c8c8;
    --white: #f6f6f6;
    --blue: #1a3fbf;
    --blue-deep: #0b31c4;
    --orange: #f57a1a;
  }
  * { box-sizing: border-box; margin: 0; padding: 0; }
  html, body { width: 1200px; height: 738px; overflow: hidden; }
  body {
    background: var(--backdrop);
    font-family: "Signika", "Trebuchet MS", sans-serif;
    font-weight: 600;
    position: relative;
  }
  .banner {
    position: absolute;
    top: 61px;
    width: 260px;
    height: 608px;
    background: linear-gradient(180deg, #fff 45%, var(--white));
    overflow: hidden;
    box-shadow: 0 2px 6px rgba(0,0,0,.12);
  }
  .banner--first { left: 56px; top: 70px; transform: scale(0.88, 0.937); transform-origin: top left; }
  .banner--values { left: 310px; }
  .banner--services { left: 610px; }
  .banner--goals { left: 910px; }
  .banner__art { position: absolute; left: 0; top: 0; width: 260px; height: 345px; display: block; }

  .values { position: absolute; left: 34px; top: 341px; list-style: none; }
  .values li { display: flex; align-items: center; height: 45px; font-size: 22px; color: var(--blue); }
  .values .icon {
    width: 24px; height: 24px; border-radius: 50%;
    background: var(--orange); margin-right: 16px;
    box-shadow: 0 0 0 3px #e4e4e4; flex: none;
  }
  .services { position: absolute; left: 23px; top: 340px; list-style: none; }
  .services li { display: flex; align-items: center; height: 25.6px; font-size: 17.5px; color: var(--blue); }
  .services li::before {
    content: ""; width: 15px; height: 15px; border-radius: 50%;
    background: var(--orange); margin-right: 6px; flex: none;
  }
  .goal { position: absolute; left: 0; width: 260px; text-align: center; font-size: 17px; line-height: 20px; }
  .goal--mission { top: 352px; color: var(--orange); }
  .goal--heritage { top: 465px; color: var(--blue); }

  .brand { position: absolute; left: 0; width: 260px; display: flex; justify-content: center; align-items: center; color: var(--blue); }
  .banner--values .brand, .banner--first .brand { top: 545px; }
  .banner--services .brand { top: 553px; }
  .banner--goals .brand { top: 545px; }
  .brand__dot { width: 30px; height: 30px; border-radius: 50%; background: var(--orange); margin-right: 8px; }
  .brand__name { font-size: 19px; line-height: 18px; }
  .brand__name small { display: block; font-size: 11.5px; letter-spacing: 1.6px; line-height: 14px; }
</style>
</head>
<body>

<svg width="0" height="0" style="position:absolute">
  <defs>
    <linearGradient id="wave-orange" x1="0" y1="0" x2="1" y2="0">
      <stop offset="0" stop-color="#ff8a1e"/><stop offset="1" stop-color="#f0641a"/>
    </linearGradient>
    <linearGradient id="photo-autumn" x1="0" y1="0" x2="0" y2="1">
      <stop offset="0" stop-color="#b8321a"/><stop offset=".6" stop-color="#d9621f"/><stop offset="1" stop-color="#e6b07a"/>
    </linearGradient>
    <linearGradient id="photo-forest" x1="0" y1="0" x2="0" y2="1">
      <stop offset="0" stop-color="#2c3a2c"/><stop offset=".6" stop-color="#3f5a3a"/><stop offset="1" stop-color="#9fb8bc"/>
    </linearGradient>
    <linearGradient id="photo-beach" x1="0" y1="0" x2="0" y2="1">
      <stop offset="0" stop-color="#4aa3d6"/><stop offset=".45" stop-color="#c9dde8"/><stop offset=".7" stop-color="#8a7a68"/><stop offset="1" stop-color="#cdb89c"/>
    </linearGradient>
    <path id="photo-area" d="M0 0 H260 V292 C200 298 140 302 100 282 C70 264 40 234 0 239 Z"/>
    <g id="banner-frame">
      <path d="M0 0 H84 C62 18 32 30 0 40 Z" fill="url(#wave-orange)"/>
      <path d="M44 0 H108 C92 7 72 12 54 15 C68 9 62 4 44 0 Z" fill="var(--blue-deep)"/>
      <path d="M110 302 L260 192 V294 Z" fill="var(--blue-deep)"/>
      <path d="M0 239 C40 232 70 262 100 282 C140 302 200 298 260 290 V296 C200 312 140 340 80 340 C45 340 25 308 0 306 Z" fill="url(#wave-orange)"/>
    </g>
  </defs>
</svg>

<!-- Values banner (roll-up) -->
<section class="banner banner--first">
  <svg class="banner__art" viewBox="0 0 260 345">
    <use href="#photo-area" fill="url(#photo-autumn)" role="img" aria-label="Photo of an autumn forest path lined with red and orange trees"/>
    <use href="#banner-frame"/>
  </svg>
  <ul class="values">
    <li><span class="icon"></span>Integrity</li>
    <li><span class="icon"></span>Transparency</li>
    <li><span class="icon"></span>Respect</li>
    <li><span class="icon"></span>Trust</li>
  </ul>
  <div class="brand"><span class="brand__dot"></span><span class="brand__name">Norvale Services<small>Limited Partnership</small></span></div>
</section>

<!-- Values banner -->
<section class="banner banner--values">
  <svg class="banner__art" viewBox="0 0 260 345">
    <use href="#photo-area" fill="url(#photo-autumn)" role="img" aria-label="Photo of an autumn forest path lined with red and orange trees"/>
    <use href="#banner-frame"/>
  </svg>
  <ul class="values">
    <li><span class="icon"></span>Integrity</li>
    <li><span class="icon"></span>Transparency</li>
    <li><span class="icon"></span>Respect</li>
    <li><span class="icon"></span>Trust</li>
  </ul>
  <div class="brand"><span class="brand__dot"></span><span class="brand__name">Norvale Services<small>Limited Partnership</small></span></div>
</section>

<!-- Services banner -->
<section class="banner banner--services">
  <svg class="banner__art" viewBox="0 0 260 345">
    <use href="#photo-area" fill="url(#photo-forest)" role="img" aria-label="Photo of a rushing river in front of a dense evergreen forest"/>
    <use href="#banner-frame"/>
  </svg>
  <ul class="services">
    <li>Pipeline Construction</li>
    <li>Road Maintenance</li>
    <li>Pipeline Clearing</li>
    <li>Land Clearing</li>
    <li>Reclamation</li>
    <li>Civil Works</li>
    <li>Mulching</li>
    <li>Logging</li>
  </ul>
  <div class="brand"><span class="brand__dot"></span><span class="brand__name">Norvale Services<small>Limited Partnership</small></span></div>
</section>

<!-- Goals banner -->
<section class="banner banner--goals">
  <svg class="banner__art" viewBox="0 0 260 345">
    <use href="#photo-area" fill="url(#photo-beach)" role="img" aria-label="Photo of a tropical beach with palm trees, rocks and blue sky"/>
    <use href="#banner-frame"/>
  </svg>
  <p class="goal goal--mission">To build and grow a strong<br>regional business providing<br>the best quality for our<br>people and clients.</p>
  <p class="goal goal--heritage">Honouring the interests of<br>Indigenous people</p>
  <div class="brand"><span class="brand__dot"></span><span class="brand__name">Norvale Services<small>Limited Partnership</small></span></div>
</section>

</body>
</html>
```